Industrial Laundry News Paper Add

We need a color add for 1/4 page newspaper using blue and white. We are an industrial laundry providing linen washing for condo rental companies. We can provide linen rental and wash customer-owned goods

```html
<!DOCTYPE html>
<html lang="en">
<head>
<meta charset="utf-8">
<title>Summit Ridge Services – Industrial Laundry Ad</title>
<link href="https://fonts.googleapis.com/css2?family=Montserrat:wght@300;400;500;600&display=swap" rel="stylesheet">
<style>
  :root {
    --stage: #5b5b5b;
    --navy: #1f2d84;
    --navy-mid: #283c9c;
    --navy-soft: #3049a8;
    --white: #ffffff;
    --steel-light: #dfe3e8;
    --steel-mid: #9aa3ad;
    --steel-dark: #4b535d;
  }
  html, body {
    margin: 0;
    padding: 0;
    width: 1200px;
    height: 2400px;
    overflow: hidden;
    background: var(--stage);
    font-family: "Montserrat", sans-serif;
  }
  .ad-frame {
    position: absolute;
    left: 50px;
    top: 488px;
    width: 1100px;
    height: 1424px;
    box-shadow: 0 10px 30px rgba(0,0,0,0.45);
  }
  .ad {
    position: absolute;
    left: 0;
    top: 0;
    width: 950px;
    height: 1230px;
    transform: scale(1.1579);
    transform-origin: 0 0;
    background: var(--navy);
    overflow: hidden;
    color: var(--white);
  }
  .ad-shapes {
    position: absolute;
    inset: 0;
  }
  .brand-seal {
    position: absolute;
    left: 540px;
    top: 520px;
    width: 360px;
    height: 360px;
    border-radius: 50%;
    background: var(--white);
    box-shadow: 0 0 0 16px var(--navy-mid);
    display: flex;
    align-items: center;
    justify-content: center;
    text-align: center;
  }
  .brand-name {
    font-weight: 600;
    font-size: 36px;
    line-height: 1.15;
    color: var(--navy);
    letter-spacing: 0.5px;
  }
  .headline {
    position: absolute;
    left: 73px;
    top: 790px;
    margin: 0;
    font-weight: 400;
  }
  .headline-lead {
    display: block;
    font-weight: 300;
    font-size: 44px;
    line-height: 60px;
  }
  .headline-main {
    display: block;
    font-weight: 500;
    font-size: 45px;
    line-height: 62px;
  }
  .service-list {
    position: absolute;
    top: 925px;
    margin: 0;
    padding: 0;
    list-style: none;
    font-weight: 300;
    font-size: 21px;
  }
  .service-list li {
    position: relative;
    padding-left: 26px;
    line-height: 30px;
  }
  .service-list li::before {
    content: "✓";
    position: absolute;
    left: 0;
    top: 0;
    font-weight: 400;
  }
  .service-list--left { left: 73px; }
  .service-list--left li { margin-bottom: 16px; }
  .service-list--right { left: 506px; width: 400px; }
  .service-list--right li { margin-bottom: 6px; }
  .divider {
    position: absolute;
    left: 72px;
    top: 1075px;
    width: 808px;
    height: 1px;
    background: rgba(255,255,255,0.7);
  }
  .contact-block {
    position: absolute;
    font-weight: 500;
    font-size: 18px;
    line-height: 23px;
  }
  .contact-row {
    position: relative;
    padding-left: 24px;
  }
  .contact-row svg {
    position: absolute;
    left: 0;
    top: 4px;
  }
  .contact-block--address { left: 70px; top: 1103px; }
  .contact-block--address .contact-row + .contact-row { margin-top: 19px; }
  .contact-split {
    position: absolute;
    left: 468px;
    top: 1110px;
    width: 1px;
    height: 82px;
    background: rgba(255,255,255,0.8);
  }
  .contact-block--reach { left: 538px; top: 1108px; }
  .phone {
    position: relative;
    padding-left: 48px;
    font-size: 37px;
    line-height: 44px;
    font-weight: 500;
  }
  .phone svg { position: absolute; left: 0; top: 6px; }
  .web {
    position: relative;
    padding-left: 30px;
    margin-top: 6px;
    font-size: 18px;
  }
  .web svg { position: absolute; left: 0; top: 4px; }
</style>
</head>
<body>
  <div class="ad-frame">
    <div class="ad">
      <svg class="ad-shapes" width="950" height="1230" viewBox="0 0 950 1230" aria-hidden="false">
        <defs>
          <linearGradient id="photoTone" x1="0" y1="0" x2="1" y2="1">
            <stop offset="0" stop-color="#c9ced4"/>
            <stop offset="0.45" stop-color="#8d959f"/>
            <stop offset="0.75" stop-color="#b9c0c8"/>
            <stop offset="1" stop-color="#5e6670"/>
          </linearGradient>
        </defs>
        <path class="photo-rim" d="M0 0 H912 C958 220 925 440 780 575 C650 700 430 760 250 745 C150 735 60 710 0 680 Z" fill="#2b3f9f"/>
        <path class="photo-area" role="img" aria-label="Photograph of a row of stainless steel front-loading industrial washing machines with open glass doors"
              d="M0 0 H892 C932 210 902 420 762 555 C640 672 420 728 250 715 C150 707 60 682 0 652 Z" fill="url(#photoTone)"/>
        <path class="lower-wave" d="M950 700 C850 880 700 980 540 1050 C700 1030 860 960 950 880 Z" fill="#2a3d9d" opacity="0.5"/>
      </svg>

      <div class="brand-seal">
        <div class="brand-name">SUMMIT RIDGE<br>SERVICES</div>
      </div>

      <h1 class="headline">
        <span class="headline-lead">The First Name</span>
        <span class="headline-main">In Industrial Laundry</span>
      </h1>

      <ul class="service-list service-list--left">
        <li>Commercial Laundry</li>
        <li>Carpet Cleaning</li>
        <li>Housekeeping In Pine Hollow</li>
      </ul>

      <ul class="service-list service-list--right">
        <li>Linen washing for condo rental companies</li>
        <li>Linen rental and wash customer -owned goods</li>
      </ul>

      <div class="divider"></div>

      <div class="contact-block contact-block--address">
        <div class="contact-row">
          <svg width="12" height="16" viewBox="0 0 12 16"><circle cx="6" cy="5" r="4" fill="none" stroke="#fff" stroke-width="1.6"/><path d="M6 9 V15 M2 15 H10" stroke="#fff" stroke-width="1.6" fill="none"/></svg>
          Alpine Crest Partners, Inc.<br>Pine Hollow, CA 90000, USA
        </div>
        <div class="contact-row">
          <svg width="14" height="11" viewBox="0 0 14 11"><rect x="0.8" y="0.8" width="12.4" height="9.4" fill="none" stroke="#fff" stroke-width="1.4"/><path d="M1 1 L7 6 L13 1" fill="none" stroke="#fff" stroke-width="1.4"/></svg>
          info@summitridgeservices.com
        </div>
      </div>

      <div class="contact-split"></div>

      <div class="contact-block contact-block--reach">
        <div class="phone">
          <svg width="34" height="34" viewBox="0 0 34 34"><circle cx="17" cy="17" r="15" fill="none" stroke="#fff" stroke-width="2.2"/><path d="M11 9 L14 9 L15.5 13 L13.5 14.5 C14.5 17 16.5 19.5 19.5 20.5 L21 18.5 L25 20 L25 23 C25 24.5 23.5 25.5 22 25 C15 23.5 10.5 18.5 9.5 12 C9.3 10.5 10 9 11 9 Z" fill="none" stroke="#fff" stroke-width="1.8" stroke-linejoin="round"/></svg>
          +1.5550142800
        </div>
        <div class="web">
          <svg width="18" height="18" viewBox="0 0 18 18"><circle cx="9" cy="9" r="7.8" fill="none" stroke="#fff" stroke-width="1.4"/><ellipse cx="9" cy="9" rx="3.4" ry="7.8" fill="none" stroke="#fff" stroke-width="1.2"/><path d="M1.2 9 H16.8 M2.5 5 H15.5 M2.5 13 H15.5" stroke="#fff" stroke-width="1.1"/></svg>
          www.SummitRidgeServices.com
        </div>
      </div>
    </div>
  </div>
</body>
</html>
```